Business / Discount Card

Looking to create a 2 sided business card. Front side to say "Thanks for flying with Skyward Drifts" then have link to "In-Flight Photos, www.skywarddrifts-example.com.au, password: skyward" Back side of card to have company logo, phone number, facebook & instagram logo and #skywarddrifts. Also included on this side will be discount text "Book again and save 10%. Use discount code: skyward10"Round Corner Card Templates are attached. Please ensure dimensions are correct.Thanks,

Font styles to use
Sans Serif

Colors
33a6d7
ffffff
000000

Requirements
Must have
• Logo
• Blue, White and Black color scheme

```html
<!DOCTYPE html>
<html lang="en">
<head>
<meta charset="utf-8">
<title>Skyward Drifts – Business Card</title>
<link rel="stylesheet" href="https://fonts.googleapis.com/css2?family=Lato:wght@400;700&family=Roboto:wght@400;500&display=swap">
<style>
  :root {
    --stage: #161616;
    --card-top: #262626;
    --card-bottom: #181818;
    --ink-white: #f2f2f2;
    --ink-soft: #c9c9c9;
    --ink-muted: #5e5e5e;
    --logo-ink: #8c8c8c;
    --rule: #6a6a6a;
    --accent: #33a6d7;
  }
  * { box-sizing: border-box; margin: 0; padding: 0; }
  html, body { width: 1200px; height: 900px; overflow: hidden; }
  body {
    background: radial-gradient(ellipse at 50% 30%, #2a2a2a 0%, var(--stage) 70%);
    font-family: "Lato", sans-serif;
    position: relative;
  }
  .card {
    position: absolute;
    left: 250px;
    width: 700px;
    height: 400px;
    border-radius: 18px;
    background: linear-gradient(135deg, var(--card-top) 0%, var(--card-bottom) 100%);
    box-shadow: 0 18px 40px rgba(0,0,0,0.6);
    overflow: hidden;
  }
  .card--back { top: 40px; }
  .card--front { top: 470px; }

  .brand-name {
    font-family: "Roboto", sans-serif;
    font-weight: 500;
    color: var(--logo-ink);
    letter-spacing: 1px;
    display: flex;
    align-items: center;
    gap: 14px;
    white-space: nowrap;
  }
  .brand-dot {
    width: 34px; height: 34px;
    border-radius: 50%;
    background: var(--logo-ink);
    flex: none;
  }

  /* back side */
  .card--back .brand-name {
    position: absolute;
    top: 130px; left: 0; right: 0;
    justify-content: center;
    font-size: 48px;
  }
  .discount-line {
    position: absolute;
    bottom: 48px; left: 0; right: 0;
    display: flex;
    justify-content: center;
    align-items: center;
    gap: 18px;
    font-family: "Roboto", sans-serif;
    font-size: 20px;
    letter-spacing: 0.5px;
    white-space: nowrap;
  }
  .discount-line .offer { color: var(--ink-muted); }
  .discount-line .divider { width: 1px; height: 30px; background: var(--rule); }
  .discount-line .code { color: var(--ink-soft); }

  /* front side */
  .card--front .brand-name {
    position: absolute;
    top: 118px; left: 40px;
    font-size: 30px;
    color: #4f4f4f;
  }
  .card--front .brand-dot { width: 26px; height: 26px; background: #4f4f4f; }
  .front-rule {
    position: absolute;
    left: 335px; top: 36px;
    width: 1px; height: 220px;
    background: var(--rule);
  }
  .contact {
    position: absolute;
    left: 360px; top: 34px;
    color: var(--ink-soft);
    white-space: nowrap;
  }
  .contact .person {
    font-family: "Roboto", sans-serif;
    font-size: 30px;
    font-weight: 400;
    letter-spacing: 2px;
    color: var(--ink-white);
    text-transform: uppercase;
  }
  .contact .role { font-size: 17px; margin-bottom: 16px; }
  .contact .address { font-size: 17px; line-height: 1.35; margin-bottom: 14px; }
  .contact ul { list-style: none; font-size: 17px; line-height: 1.5; }
  .contact li { display: flex; align-items: center; gap: 9px; }
  .contact svg { width: 12px; height: 12px; flex: none; fill: none; stroke: var(--ink-soft); stroke-width: 1.6; }

  .thanks {
    position: absolute;
    left: 40px; top: 300px;
    font-family: "Roboto", sans-serif;
    font-weight: 500;
    font-size: 19px;
    letter-spacing: 1px;
    color: var(--ink-muted);
    white-space: nowrap;
  }
  .thanks .strong { color: var(--ink-soft); }
  .photos {
    position: absolute;
    left: 40px; top: 342px;
    font-family: "Roboto", sans-serif;
    font-size: 13px;
    color: var(--ink-soft);
    white-space: nowrap;
  }
  .photos .label { color: var(--accent); font-weight: 500; }
  .social {
    position: absolute;
    right: 40px; top: 294px;
    display: flex; gap: 14px;
  }
  .social span {
    width: 32px; height: 32px;
    border-radius: 6px;
    background: var(--accent);
  }
  .hashtag {
    position: absolute;
    right: 40px; top: 340px;
    font-family: "Roboto", sans-serif;
    font-size: 15px;
    color: var(--ink-white);
    white-space: nowrap;
  }
</style>
</head>
<body>

  <section class="card card--back">
    <div class="brand-name"><span class="brand-dot"></span>Skyward Drifts</div>
    <p class="discount-line">
      <span class="offer">Book again and save 10%.</span>
      <span class="divider"></span>
      <span class="code">Use discount code: skyward10</span>
    </p>
  </section>

  <section class="card card--front">
    <div class="brand-name"><span class="brand-dot"></span>Skyward Drifts</div>
    <div class="front-rule"></div>
    <div class="contact">
      <h1 class="person">Daniel Harper</h1>
      <p class="role">Director</p>
      <p class="address">PO Box 812,<br>Ridgevale, NSW, 2410</p>
      <ul>
        <li><svg viewBox="0 0 14 14"><path d="M3 1.5 L5 1.5 L6 4.5 L4.5 5.5 Q5.5 8.5 8.5 9.5 L9.5 8 L12.5 9 L12.5 11 Q12 12.5 10 12.5 Q2 11.5 1.5 4 Q1.5 2 3 1.5 Z"/></svg>1300 555 019</li>
        <li><svg viewBox="0 0 14 14"><rect x="1" y="3" width="12" height="8"/><path d="M1 3 L7 8 L13 3"/></svg>info@skywarddrifts-example.com.au</li>
        <li><svg viewBox="0 0 14 14"><circle cx="7" cy="7" r="5.5"/><path d="M1.5 7 H12.5 M7 1.5 Q4 7 7 12.5 M7 1.5 Q10 7 7 12.5"/></svg>www.skywarddrifts-example.com.au</li>
      </ul>
    </div>
    <p class="thanks">Thanks for flying with <span class="strong">Skyward Drifts</span></p>
    <p class="photos"><span class="label">In-Flight Photos:</span> www.skywarddrifts-example.com.au · password: skyward</p>
    <div class="social" aria-label="Social media links">
      <span></span><span></span>
    </div>
    <p class="hashtag">#skywarddrifts</p>
  </section>

</body>
</html>
```